Tavo Payments Business card refresh

Need a new design of our business card The info is not what is on these cards i sent this for a reference. I can email all the info over
Info would be Derek Whitfield Chief TAVO is the title. our new address is 47615 Birch Hollow Rd. Cedar Ridge Village Ca 91384 Cell number is 805-634-2917 Work number is 855-482-7309 ext 212 Derek@tavopayments.com is my email address
Target Market(s)
Merchant Services all businesses that take credit cards
Industry/Entity Type
Merchant Services / Credit Card processing
Contact Information for Business Card
Need a new design of our business card The info is not what is on these cards i sent this for a reference. I can email all the info over Info would be Derek Whitfield Chief TAVO is the title. our new address is 47615 Birch Hollow Rd. Cedar Ridge Village Ca 91384 Cell number is 805-634-2917 Work number is 855-482-7309 ext 212 Derek@tavopayments.com is my email address
Requirements
Must have
- My logo and colors from my brand guidelines
Nice to have
- i sent some designs just need a new refresh
Should not have
- nothing specific

```html
<!DOCTYPE html>
<html lang="en">
<head>
<meta charset="utf-8">
<title>Tavo Payments — Business Card</title>
<link href="https://fonts.googleapis.com/css2?family=Lato:wght@300;400;700;900&display=swap" rel="stylesheet">
<style>
  :root {
    --backdrop: #e9d3c2;
    --card: #262a35;
    --card-deep: #1f222b;
    --white: #ffffff;
    --lime: #9ccc12;
    --muted: #d9dbe0;
  }
  * { margin: 0; padding: 0; box-sizing: border-box; }
  html, body { width: 1200px; height: 989px; overflow: hidden; }
  body {
    background: var(--backdrop);
    font-family: "Lato", sans-serif;
    position: relative;
  }
  .card {
    position: absolute;
    left: 250px;
    width: 700px;
    height: 400px;
    background: linear-gradient(180deg, var(--card) 0%, var(--card-deep) 100%);
    box-shadow: 0 14px 30px rgba(60, 35, 20, 0.35);
    color: var(--white);
  }
  .card--front { top: 50px; }
  .card--back { top: 510px; }

  .wordmark {
    display: flex;
    align-items: center;
    gap: 14px;
    font-weight: 900;
    color: var(--white);
    letter-spacing: 0.04em;
    line-height: 1;
    white-space: nowrap;
  }
  .wordmark__dot {
    background: var(--lime);
    flex: none;
  }
  .card--front .wordmark {
    position: absolute;
    left: 50%;
    top: 50%;
    transform: translate(-50%, -50%);
    font-size: 62px;
  }
  .card--front .wordmark__dot { width: 26px; height: 26px; }

  .card--back .wordmark {
    position: absolute;
    right: 48px;
    top: 48px;
    font-size: 40px;
  }
  .card--back .wordmark__dot { width: 18px; height: 18px; }

  .address {
    position: absolute;
    right: 48px;
    top: 150px;
    text-align: right;
    font-size: 17px;
    font-style: normal;
    font-weight: 300;
    line-height: 1.45;
    color: var(--muted);
  }
  .address__web { color: var(--lime); }

  .person {
    position: absolute;
    left: 48px;
    bottom: 150px;
  }
  .person__name {
    font-size: 30px;
    font-weight: 900;
    color: var(--lime);
    letter-spacing: 0.01em;
    line-height: 1.1;
  }
  .person__title {
    font-size: 20px;
    font-weight: 400;
    color: var(--white);
    margin-top: 2px;
  }
  .person__rule {
    width: 80px;
    height: 5px;
    background: var(--lime);
    margin-top: 10px;
  }

  .contacts {
    position: absolute;
    left: 48px;
    bottom: 36px;
    list-style: none;
    font-size: 18px;
    font-weight: 300;
    color: var(--muted);
    line-height: 1.55;
  }
  .contacts__item {
    display: flex;
    align-items: center;
    gap: 12px;
  }
  .contacts__icon { width: 16px; height: 16px; flex: none; }
</style>
</head>
<body>

  <section class="card card--front" aria-label="Business card front">
    <div class="wordmark"><span class="wordmark__dot"></span>TAVO PAYMENTS</div>
  </section>

  <section class="card card--back" aria-label="Business card back">
    <div class="wordmark"><span class="wordmark__dot"></span>TAVO PAYMENTS</div>

    <address class="address">
      <div>47615 Birch Hollow Rd.</div>
      <div>Cedar Ridge Village Ca 91384</div>
      <div class="address__web">www.tavopayments.com</div>
    </address>

    <div class="person">
      <div class="person__name">DEREK WHITFIELD</div>
      <div class="person__title">Chief TAVO</div>
      <div class="person__rule"></div>
    </div>

    <ul class="contacts">
      <li class="contacts__item">
        <svg class="contacts__icon" viewBox="0 0 16 16" aria-hidden="true">
          <rect x="4" y="1" width="8" height="14" rx="1.5" fill="none" stroke="#9ccc12" stroke-width="1.6"/>
          <rect x="7" y="12" width="2" height="1.4" fill="#9ccc12"/>
        </svg>
        805-634-2917
      </li>
      <li class="contacts__item">
        <svg class="contacts__icon" viewBox="0 0 16 16" aria-hidden="true">
          <path d="M3 2 L6 2 L7 5.5 L5.2 6.8 C6 8.6 7.4 10 9.2 10.8 L10.5 9 L14 10 L14 13 C14 13.6 13.6 14 13 14 C7.5 14 2 8.5 2 3 C2 2.4 2.4 2 3 2 Z" fill="#9ccc12"/>
        </svg>
        855-482-7309 ext 212
      </li>
      <li class="contacts__item">
        <svg class="contacts__icon" viewBox="0 0 16 16" aria-hidden="true">
          <rect x="1" y="3" width="14" height="10" rx="1" fill="#9ccc12"/>
          <path d="M1.5 3.5 L8 8.8 L14.5 3.5" fill="none" stroke="#262a35" stroke-width="1.4"/>
        </svg>
        Derek@tavopayments.com
      </li>
    </ul>
  </section>

</body>
</html>
```